Business card design for new, innovative company - BluePlinth

We are a new company looking for a business card design that is fun, different and quirky. Must use corporate colour green - CMYK C:55, M:0, Y:100, K:0, and corporate colour grey - C:0, M:0, Y: 0, K:70.

We have developed the first real time data application, in which people are able to profile the data of their existing customers in order to pull out more good fit clients to direct their marketing activities at.

Industry/Entity Type

Marketing

Requirements
Must have
• Logo, name, title, telephone number, fax number, email, website, address

```html
<!DOCTYPE html>
<html lang="en">
<head>
<meta charset="utf-8">
<title>BluePlinth business card</title>
<link rel="stylesheet" href="https://fonts.googleapis.com/css2?family=Source+Sans+3:wght@300;400;700&display=swap">
<style>
  :root {
    --green: #7dc242;
    --grey: #737477;
    --ink-grey: #6d6e71;
    --label-grey: #cfcfd1;
    --paper: #ffffff;
    --stage: #fdfdfd;
  }
  * { margin: 0; padding: 0; box-sizing: border-box; }
  html, body { width: 1200px; height: 1000px; overflow: hidden; }
  body {
    position: relative;
    background: var(--stage);
    font-family: "Source Sans 3", "Helvetica Neue", Arial, sans-serif;
  }
  .side-label {
    position: absolute;
    font-weight: 300;
    font-size: 56px;
    line-height: 1;
    color: var(--label-grey);
  }
  .side-label--front { left: 124px; top: 121px; }
  .side-label--back { left: 903px; top: 126px; }

  .card {
    position: absolute;
    top: 344px;
    width: 544px;
    height: 341px;
  }
  .card--front {
    left: 64px;
    background: var(--paper);
    box-shadow: 0 0 8px rgba(0,0,0,0.22);
  }
  .card--back {
    left: 627px;
    background: var(--grey);
  }

  .sweep {
    position: absolute;
    left: 0; top: 0;
    width: 1200px; height: 1000px;
    pointer-events: none;
  }

  .front-identity {
    position: absolute;
    right: 200px;
    top: 150px;
    text-align: right;
  }
  .brand-name {
    font-weight: 700;
    letter-spacing: -1.5px;
    line-height: 1;
  }
  .front-identity .brand-name {
    font-size: 64px;
    color: var(--green);
  }
  .person-name {
    margin-top: 8px;
    font-size: 28px;
    font-weight: 400;
    color: var(--ink-grey);
    line-height: 1;
  }
  .person-title {
    margin-top: 5px;
    font-size: 15px;
    color: var(--green);
    line-height: 1;
  }

  .contact-list {
    position: absolute;
    right: 36px;
    top: 45px;
    list-style: none;
    text-align: right;
    font-size: 15.5px;
    line-height: 19.7px;
    color: var(--green);
  }
  .back-brand {
    position: absolute;
    right: 38px;
    top: 166px;
    font-size: 37px;
    color: #ffffff;
  }
</style>
</head>
<body>
  <div class="side-label side-label--front">front</div>
  <div class="side-label side-label--back">back</div>

  <section class="card card--front">
    <div class="front-identity">
      <div class="brand-name">BluePlinth</div>
      <div class="person-name">Your Name</div>
      <div class="person-title">Chief Consultant</div>
    </div>
  </section>

  <section class="card card--back">
    <ul class="contact-list">
      <li>Email: info@blueplinth.com</li>
      <li>Mobile Phone: +44 (0) 00000000</li>
      <li>Website: www.blueplinth.com</li>
      <li>Chirper: @blueplinth</li>
      <li>Social: www.friendspage.com/blueplinth</li>
    </ul>
    <div class="brand-name back-brand">BluePlinth</div>
  </section>

  <svg class="sweep" viewBox="0 0 1200 1000" aria-hidden="true">
    <defs>
      <clipPath id="card-areas">
        <rect x="64" y="344" width="544" height="341"/>
        <rect x="627" y="344" width="544" height="341"/>
      </clipPath>
    </defs>
    <path class="sweep-band" clip-path="url(#card-areas)" fill="var(--green)"
          d="M540 700 C600 560, 700 400, 880 322 L896 338 C730 420, 640 560, 574 700 Z"/>
  </svg>
</body>
</html>
```